Loud Kite Promotional Banner

We are looking for a design for a 33.5" x 79" retractable pop-up banners to used at our live shows. We are a cover band that performs at clubs, corporate events, private parties, and weddings. We would have 2 banners, one on each side of the drum riser, and placed between the lighting trusses. Our website and Facebook page will provide information on what we are about - high energy fun entertainment of live music. We would like some marketing on the banner with logos, etc - something classy that can be used at almost any event. Contact information on the banners would be great. The banners do not have to be the exact same.

Website: www. loudkiteband.example
FB: https://www.social.example/Loudkitebandplano

I have uploaded a logo that can be used. Any other information, images, etc are available not the sites too.

Target Market(s)

New clients looking for a live band

Industry/Entity Type

Live Entertainment

Colors
0054AA
0677BA
7BADD7
CADEEF
E8F1F8
0094D4
00A9DD
6FCCEA
C7EBF8
E9F6FB

Requirements
Must have
• Logo, website address
Nice to have
• Images and excitement

```html
<!DOCTYPE html>
<html lang="en">
<head>
<meta charset="utf-8">
<title>Loud Kite Pop-up Banners</title>
<link rel="stylesheet" href="https://fonts.googleapis.com/css2?family=Noto+Serif:wght@700&display=swap">
<style>
  :root {
    --page: #ffffff;
    --plate-light: #e4e4e4;
    --plate-mid: #b9b9b9;
    --plate-dark: #8d8d8d;
    --band-dark: #0a0a0a;
    --band-grey: #5a5a5a;
    --blue-deep: #0054aa;
    --blue-bright: #00a9dd;
    --cassette-shell: #4f5054;
    --cassette-window: #8ad6f5;
    --ink: #111111;
    --frame: #3a3a3a;
    --dot: #0677ba;
  }
  html, body {
    margin: 0;
    width: 1200px;
    height: 1074px;
    overflow: hidden;
    background: var(--page);
  }
  .sheet {
    position: relative;
    width: 1200px;
    height: 1074px;
  }
  .banner {
    position: absolute;
    top: 94px;
    width: 508px;
    height: 875px;
  }
  .banner--left { left: 80px; }
  .banner--right { left: 613px; }
  .banner svg { display: block; width: 100%; height: 100%; }
  .brand-name, .web-address, .social-handle {
    font-family: "Noto Serif", Georgia, serif;
    font-weight: 700;
    fill: var(--ink);
  }
</style>
</head>
<body>
<main class="sheet">
  <section class="banner banner--left" aria-label="Loud Kite banner">
    <svg viewBox="0 0 846 1458" xmlns="http://www.w3.org/2000/svg">
      <defs>
        <linearGradient id="plate-left" x1="0" y1="0" x2="1" y2="1">
          <stop offset="0" stop-color="var(--plate-dark)"/>
          <stop offset="0.35" stop-color="var(--plate-light)"/>
          <stop offset="0.6" stop-color="var(--plate-mid)"/>
          <stop offset="0.85" stop-color="var(--plate-light)"/>
          <stop offset="1" stop-color="var(--plate-dark)"/>
        </linearGradient>
        <linearGradient id="dark-left" x1="0" y1="1" x2="1" y2="0">
          <stop offset="0" stop-color="var(--band-dark)"/>
          <stop offset="1" stop-color="var(--band-grey)"/>
        </linearGradient>
        <linearGradient id="blue-left" x1="0" y1="0" x2="1" y2="0">
          <stop offset="0" stop-color="var(--blue-bright)"/>
          <stop offset="1" stop-color="var(--blue-deep)"/>
        </linearGradient>
        <linearGradient id="cassette-left" x1="0" y1="0" x2="0" y2="1">
          <stop offset="0" stop-color="var(--cassette-shell)"/>
          <stop offset="0.15" stop-color="var(--cassette-window)"/>
          <stop offset="0.68" stop-color="var(--cassette-window)"/>
          <stop offset="0.75" stop-color="var(--cassette-shell)"/>
        </linearGradient>
      </defs>
      <rect class="plate" width="846" height="1458" fill="url(#plate-left)" role="img" aria-label="Brushed diamond-plate metal texture"/>
      <polygon class="band-accent" points="846,312 426,387 846,458" fill="url(#blue-left)"/>
      <polygon class="band-dark" points="0,458 426,387 846,458 846,996 420,1066 0,996" fill="url(#dark-left)"/>
      <polygon class="band-accent" points="0,996 420,1066 0,1142" fill="url(#blue-left)"/>
      <rect class="cassette" x="80" y="497" width="686" height="442" rx="40" fill="url(#cassette-left)" stroke="var(--ink)" stroke-width="4" role="img" aria-label="Illustrated cassette tape"/>
      <text class="brand-name" x="423" y="590" text-anchor="middle" font-size="58" letter-spacing="10">LOUD KITE</text>
      <text class="web-address" x="423" y="1244" text-anchor="middle" font-size="40" textLength="640" lengthAdjust="spacing">www.loudkiteband.example</text>
      <path class="handle-frame" d="M355 1287 H127 a4 4 0 0 0 -4 4 V1368 a4 4 0 0 0 4 4 H719 a4 4 0 0 0 4 -4 V1291 a4 4 0 0 0 -4 -4 H493" fill="none" stroke="var(--frame)" stroke-width="2.5"/>
      <circle class="social-dot" cx="424" cy="1287" r="19" fill="var(--dot)"/>
      <text class="social-handle" x="423" y="1345" text-anchor="middle" font-size="32" textLength="530" lengthAdjust="spacing">/Loudkitebandplano</text>
    </svg>
  </section>

  <section class="banner banner--right" aria-label="Loud Kite banner">
    <svg viewBox="0 0 846 1458" xmlns="http://www.w3.org/2000/svg">
      <rect class="plate" width="846" height="1458" fill="url(#plate-left)" role="img" aria-label="Brushed diamond-plate metal texture"/>
      <polygon class="band-accent" points="846,312 426,387 846,458" fill="url(#blue-left)"/>
      <polygon class="band-dark" points="0,458 426,387 846,458 846,996 420,1066 0,996" fill="url(#dark-left)"/>
      <polygon class="band-accent" points="0,996 420,1066 0,1142" fill="url(#blue-left)"/>
      <rect class="cassette" x="80" y="497" width="686" height="442" rx="40" fill="url(#cassette-left)" stroke="var(--ink)" stroke-width="4" role="img" aria-label="Illustrated cassette tape"/>
      <text class="brand-name" x="423" y="590" text-anchor="middle" font-size="58" letter-spacing="10">LOUD KITE</text>
      <text class="web-address" x="423" y="1244" text-anchor="middle" font-size="40" textLength="640" lengthAdjust="spacing">www.loudkiteband.example</text>
      <path class="handle-frame" d="M355 1287 H127 a4 4 0 0 0 -4 4 V1368 a4 4 0 0 0 4 4 H719 a4 4 0 0 0 4 -4 V1291 a4 4 0 0 0 -4 -4 H493" fill="none" stroke="var(--frame)" stroke-width="2.5"/>
      <circle class="social-dot" cx="424" cy="1287" r="19" fill="var(--dot)"/>
      <text class="social-handle" x="423" y="1345" text-anchor="middle" font-size="32" textLength="530" lengthAdjust="spacing">/Loudkitebandplano</text>
    </svg>
  </section>
</main>
</body>
</html>
```